Kestrel Signs Facebook Banner Design

Design a facebook banner for a sign company. I would like to have a modern approach to it.

Product Offering:
Signs
Banners
Decals
Commercial Wraps

```html
<!DOCTYPE html>
<html lang="en">
<head>
<meta charset="utf-8">
<title>Kestrel Signs – Facebook Banner</title>
<link href="https://fonts.googleapis.com/css2?family=Russo+One&family=Questrial&display=swap" rel="stylesheet">
<style>
  :root {
    --page: #ffffff;
    --banner-center: #3d4245;
    --banner-edge: #242935;
    --brand-red: #e5333a;
    --text-white: #ffffff;
    --pill-red: #e0261c;
    --pill-orange: #f28a12;
    --pill-yellow: #ffe600;
    --card-edge: #ffffff;
  }
  html, body {
    margin: 0;
    padding: 0;
    width: 1200px;
    height: 1200px;
    overflow: hidden;
    background: var(--page);
  }
  .canvas {
    position: relative;
    width: 1200px;
    height: 1200px;
    background: var(--page);
  }
  .banner {
    position: absolute;
    left: 35px;
    top: 391px;
    width: 1130px;
    height: 418px;
    background: radial-gradient(ellipse 55% 70% at 40% 55%, var(--banner-center) 0%, var(--banner-edge) 100%);
    overflow: hidden;
  }
  .brand {
    position: absolute;
    left: 80px;
    top: 40px;
    width: 570px;
    text-align: center;
    font-family: "Russo One", sans-serif;
    line-height: 1;
  }
  .brand-name {
    display: block;
    font-size: 84px;
    color: var(--brand-red);
    letter-spacing: 2px;
  }
  .brand-sub {
    display: block;
    margin-top: 10px;
    font-size: 64px;
    color: var(--text-white);
    letter-spacing: 2px;
  }
  .offer-pill {
    position: absolute;
    left: 215px;
    top: 214px;
    width: 281px;
    height: 38px;
    border-radius: 19px;
    background: linear-gradient(90deg, var(--pill-red) 0%, var(--pill-orange) 35%, var(--pill-yellow) 55%, var(--pill-orange) 75%, var(--pill-red) 100%);
    color: var(--text-white);
    font-family: "Questrial", sans-serif;
    font-size: 22px;
    line-height: 38px;
    text-align: center;
    letter-spacing: 0.5px;
  }
  .product-list {
    position: absolute;
    left: 0;
    top: 285px;
    width: 730px;
    margin: 0;
    padding: 0;
    list-style: none;
    font-family: "Questrial", sans-serif;
    font-size: 34px;
    color: var(--text-white);
    text-align: center;
    line-height: 60px;
  }
  .product-list li {
    display: inline-block;
    margin: 0 9px;
  }
  .product-list li::before {
    content: "";
    display: inline-block;
    width: 4px;
    height: 28px;
    margin-right: 8px;
    background: var(--brand-red);
    vertical-align: -3px;
  }
  .showcase {
    position: absolute;
    border: 2px solid var(--card-edge);
    box-sizing: border-box;
  }
  .showcase-storefront {
    left: 727px;
    top: 22px;
    width: 318px;
    height: 180px;
    border-radius: 34px;
    transform: rotate(-4deg);
    background: linear-gradient(180deg, #2f6ec9 0%, #4b8ad8 55%, #5a3a2c 56%, #3b2a22 100%);
  }
  .showcase-wrap {
    left: 712px;
    top: 236px;
    width: 325px;
    height: 160px;
    border-radius: 30px;
    transform: rotate(-4deg);
    background: linear-gradient(135deg, #f1f1f1 0%, #d9d9db 45%, #d63a3a 60%, #ececec 100%);
  }
  .showcase-stickers {
    left: 918px;
    top: 196px;
    width: 198px;
    height: 82px;
    border-radius: 41px;
    transform: rotate(-3deg);
    background: linear-gradient(90deg, #f7f7f7 0%, #ececec 100%);
  }
  .showcase-sale {
    left: 598px;
    top: 181px;
    width: 198px;
    height: 88px;
    border-radius: 44px;
    transform: rotate(-7deg);
    background: linear-gradient(90deg, #3a0c0e 0%, #8e1418 55%, #b81d22 100%);
  }
</style>
</head>
<body>
  <main class="canvas">
    <section class="banner">
      <h1 class="brand">
        <span class="brand-name">KESTREL</span>
        <span class="brand-sub">SIGNS</span>
      </h1>

      <div class="offer-pill">PRODUCT OFFERING</div>

      <ul class="product-list">
        <li>SIGNS</li>
        <li>BANNERS</li>
        <li>DECALS</li>
        <li>COMMERCIAL WRAPS</li>
      </ul>

      <div class="showcase showcase-storefront" role="img" aria-label="Photo of a storefront pylon sign with several tenant panels against a blue sky"></div>
      <div class="showcase showcase-wrap" role="img" aria-label="Illustration of a white sports car with a red and black commercial vinyl wrap"></div>
      <div class="showcase showcase-stickers" role="img" aria-label="Sample of printed vinyl decal stickers on a white backing"></div>
      <div class="showcase showcase-sale" role="img" aria-label="Sample of a dark red seasonal sale banner graphic"></div>
    </section>
  </main>
</body>
</html>
```